Mobil Battery Sales and Instalation

We are a automotive roadside svc company. I am looking to focus on battery sales and instalation We offer tire changes, lockuot, jump starts fuel delivry and battery sales This design should be battery sales and instalation focused My company name is. Ridgeway Roadside Svcs. 707-216-3847 call or text Hours 7am to 9pm. Free service call and instalation with purchase of new battery. Free testing Free battery disposal Colors we like are black and orange or red and black

Target Market(s)

Automotive, RV, Comerical truck, motorcycle and boat

Industry/Entity Type

Automotive

Requirements
Must have
• Pic of battery
• Mobil battery service.
Nice to have
• I want people to see this card and know its a mobil service for battery sales and installation. But can see we offer other services.
• Use my company name but i dont want that to be the standout. (Tuck it in somewhere).
Should not have
• No pictures of any trucks cars etc.
• we do not tow!

```html
<!DOCTYPE html>
<html lang="en">
<head>
<meta charset="utf-8">
<title>Ridgeway Roadside Svcs – Mobile Battery Service Card</title>
<link rel="stylesheet" href="https://fonts.googleapis.com/css2?family=Oswald:wght@400;500&family=Questrial&family=Tinos:wght@700&display=swap">
<style>
  :root {
    --page-bg: #2b2b2b;
    --card-bg: #ffffff;
    --panel-grey: #eeeeee;
    --orange: #f47a20;
    --red: #e1261c;
    --ink: #1c1c1c;
    --white: #ffffff;
    --muted-ring: #fbd2a9;
  }
  * { box-sizing: border-box; margin: 0; padding: 0; }
  html, body {
    width: 1125px; height: 1200px; overflow: hidden;
    background: var(--page-bg);
  }
  .card {
    position: absolute; left: 40px; top: 249px;
    width: 1045px; height: 702px;
    background: var(--card-bg);
    overflow: hidden;
    font-family: "Questrial", sans-serif;
  }
  .card-shapes { position: absolute; inset: 0; }

  .brand { position: absolute; left: 58px; top: 40px; }
  .brand-name {
    font-family: "Questrial", sans-serif;
    font-size: 62px; line-height: 1; color: var(--orange);
    letter-spacing: 1px;
  }
  .brand-tag {
    font-family: "Tinos", serif; font-weight: 700;
    font-size: 35px; color: var(--ink); margin-top: 14px; margin-left: 2px;
  }

  .markets {
    position: absolute; left: 557px; top: 36px;
    font-family: "Oswald", sans-serif; font-weight: 400;
    font-size: 41px; line-height: 50px; color: var(--white);
  }

  .battery-photo {
    position: absolute; left: 612px; top: 172px;
    width: 420px; height: 325px;
    background: radial-gradient(ellipse at 50% 50%, #cfcfcf 0%, #a9a9a9 40%, #5a5a5a 70%, #3a3a3a 100%);
    border-radius: 28px;
  }

  .service-banner {
    position: absolute; left: 47px; top: 201px;
    width: 468px; height: 130px;
    background: linear-gradient(90deg, var(--red), var(--orange));
    padding: 6px;
  }
  .service-banner-inner {
    width: 100%; height: 100%;
    border: 1.5px dashed rgba(255,255,255,0.85);
    padding: 12px 0 0 20px;
    font-family: "Oswald", sans-serif; font-weight: 400;
    font-size: 37px; line-height: 53px; color: var(--white);
  }

  .best-tag {
    position: absolute; left: 47px; top: 363px;
    width: 227px; height: 37px;
    background: var(--orange);
    color: var(--white); font-size: 25px; line-height: 37px;
    padding-left: 24px;
  }

  .service-list { position: absolute; left: 52px; top: 413px; list-style: none; }
  .service-list li {
    display: flex; align-items: center;
    height: 42px; font-size: 26px; color: var(--ink);
  }
  .service-list svg { width: 19px; height: 19px; margin-right: 11px; flex: none; }

  .perks-band {
    position: absolute; left: 0; top: 636px;
    width: 620px; height: 44px;
    background: var(--orange);
    clip-path: polygon(0 0, 582px 0, 620px 44px, 0 44px);
    color: var(--white); font-size: 25px; line-height: 44px;
    padding-left: 62px;
  }

  .offer-badge {
    position: absolute; left: 398px; top: 426px;
    width: 204px; height: 204px; border-radius: 50%;
    background: var(--muted-ring);
    display: flex; align-items: center; justify-content: center;
  }
  .offer-badge-core {
    width: 178px; height: 178px; border-radius: 50%;
    background: var(--orange);
    display: flex; align-items: center; justify-content: center; text-align: center;
    font-family: "Oswald", sans-serif; font-size: 18px; line-height: 28px; color: var(--white);
  }

  .contact-band {
    position: absolute; left: 672px; height: 46px; width: 373px;
    background: var(--orange);
    color: var(--white);
  }
  .contact-band.phone { top: 573px; font-size: 40px; line-height: 46px; padding-left: 52px; }
  .contact-band.text { top: 636px; font-size: 28px; line-height: 46px; padding-left: 52px; }
  .contact-icon { position: absolute; left: 655px; width: 50px; height: 50px; }
  .contact-icon.phone { top: 571px; }
  .contact-icon.text { top: 634px; }
</style>
</head>
<body>
<main class="card">
  <svg class="card-shapes" viewBox="0 0 1045 702" width="1045" height="702" aria-hidden="true">
    <path d="M490 0 H1045 V702 H770 L505 336 Q470 260 515 185 Q470 110 490 0 Z" fill="var(--panel-grey)"/>
    <path d="M500 26 H1045 V138 H540 Q505 90 500 26 Z" fill="var(--orange)"/>
    <path d="M400 0 H462 Q452 115 525 195 Q395 130 400 0 Z" fill="var(--orange)"/>
    <path d="M470 0 H490 Q484 100 548 165 Q462 105 470 0 Z" fill="var(--red)"/>
    <path d="M495 336 L515 336 L765 702 L730 702 Z" fill="var(--red)"/>
    <path d="M515 336 L532 340 L792 702 L765 702 Z" fill="var(--orange)"/>
  </svg>

  <div class="brand">
    <div class="brand-name">Ridgeway</div>
    <div class="brand-tag">Roadside Svcs.</div>
  </div>

  <div class="markets">FOR AUTO, COMMERCIAL,<br>MARINE/RV,POWERSPORT</div>

  <div class="battery-photo" role="img" aria-label="Photo of three car batteries with red and blue terminals"></div>

  <div class="service-banner">
    <div class="service-banner-inner">Mobil Service For<br>Battery Sales And Installation</div>
  </div>

  <div class="best-tag">We are Best in</div>

  <ul class="service-list">
    <li><svg viewBox="0 0 20 20"><circle cx="10" cy="10" r="8.5" fill="none" stroke="var(--orange)" stroke-width="2"/><path d="M5.5 10 L9 13.5 L16 5" fill="none" stroke="var(--orange)" stroke-width="2.4"/></svg>Battery Sales</li>
    <li><svg viewBox="0 0 20 20"><circle cx="10" cy="10" r="8.5" fill="none" stroke="var(--orange)" stroke-width="2"/><path d="M5.5 10 L9 13.5 L16 5" fill="none" stroke="var(--orange)" stroke-width="2.4"/></svg>Battery installation</li>
    <li><svg viewBox="0 0 20 20"><circle cx="10" cy="10" r="8.5" fill="none" stroke="var(--orange)" stroke-width="2"/><path d="M5.5 10 L9 13.5 L16 5" fill="none" stroke="var(--orange)" stroke-width="2.4"/></svg>Tire Changes</li>
    <li><svg viewBox="0 0 20 20"><circle cx="10" cy="10" r="8.5" fill="none" stroke="var(--orange)" stroke-width="2"/><path d="M5.5 10 L9 13.5 L16 5" fill="none" stroke="var(--orange)" stroke-width="2.4"/></svg>Lockout</li>
    <li><svg viewBox="0 0 20 20"><circle cx="10" cy="10" r="8.5" fill="none" stroke="var(--orange)" stroke-width="2"/><path d="M5.5 10 L9 13.5 L16 5" fill="none" stroke="var(--orange)" stroke-width="2.4"/></svg>Jump Starts Fuel Delivery</li>
  </ul>

  <div class="perks-band">Free Testing Free Battery Disposal</div>

  <div class="offer-badge">
    <div class="offer-badge-core">Free Service Call<br>And Installation<br>With Purchase Of<br>New Battery.</div>
  </div>

  <div class="contact-band phone">707-216-3847</div>
  <div class="contact-band text">or text 7am to 9pm</div>

  <svg class="contact-icon phone" viewBox="0 0 50 50" aria-hidden="true">
    <circle cx="25" cy="25" r="24" fill="var(--white)"/>
    <circle cx="25" cy="25" r="20" fill="var(--red)"/>
    <path d="M18 14 L22 14 L24 20 L21 22 Q23 27 28 29 L30 26 L36 28 L36 32 Q35 36 31 36 Q16 34 14 19 Q14 15 18 14 Z" fill="var(--white)"/>
  </svg>
  <svg class="contact-icon text" viewBox="0 0 50 50" aria-hidden="true">
    <circle cx="25" cy="25" r="24" fill="var(--white)"/>
    <circle cx="25" cy="25" r="20" fill="var(--red)"/>
    <path d="M14 15 H36 V30 H23 L17 35 V30 H14 Z" fill="none" stroke="var(--white)" stroke-width="2.4" stroke-linejoin="round"/>
    <path d="M19 20 H31 M19 25 H28" stroke="var(--white)" stroke-width="2.2"/>
  </svg>
</main>
</body>
</html>
```